Website for cloud software, Coded

We would like a website designed for an invoicing software used in the cloud. It is a new product based on a PC-loaded software that we have sold for 10 years, refer www.billquarry.example
Winner will need to code the page in HTML with everything a functional website needs.

Target Market(s)

small business owners

Industry/Entity Type

Software

Requirements
Must have
• We would need:
Homepage (description of product)
Features (to be able to put screenshots)
Pricing & Sign-up
Contact & About

Page 1 - Home page
introduction to billquarry!Sky - the next step up from PC-based billquarry (sold since 1999). Same product, but use from anywhere with any mobile device.

Page 2 - Features
provides screen shots of this extensive program and must have room for plenty of text to accompany the images. Refer www.tumbled-slate.example/features for scope. Looking for quick-load page with innovative presentation of the features

Page 3 - Pricing
includes Pricing, Sign-up, Contact and Log-in (for existing users)
Pricing has single-month price, and concession rates for signing up a year in advance
Sign-up is a link to an external page where people can try the program free for 14 days.

Page 4 Contact & About
Contact is a box for people to write to us with questions (sent to info@billquarry.example)
Log-in (for existing users) is a link to an external page where existing users can log on to their program (they will also get a shortcut from us that makes sign-on quicker).
A brief history of our Company and billquarry! software

We would like a crisp modern look for the website.
Emphasise access to software with any mobile device and from anywhere that has internet access.
Nice to have
• It should be editable in Frontpage. Pictures of stylised cloud is acceptable.
Should not have
• Website style:
we don't have any style in mind, except we DON'T want black or dark background. Fast loading, so avoid use of extensive flash stuff.

```html
<!DOCTYPE html>
<html lang="en">
<head>
<meta charset="utf-8">
<title>billquarry! – invoicing software for your business</title>
<link href="https://fonts.googleapis.com/css2?family=PT+Sans:ital,wght@0,400;0,700;1,400;1,700&family=Archivo+Black&display=swap" rel="stylesheet">
<style>
:root{
  --ink:#3a3a3a;
  --muted:#5d5d5d;
  --blue:#0a5a93;
  --blue-deep:#0b3d66;
  --band:#0b578f;
  --footer:#0a3a62;
  --link:#1b6fb5;
  --gold:#c9a400;
  --orange-top:#ffb300;
  --orange-bot:#ff8a00;
  --panel:#e9e9e9;
  --nav-top:#8c8c8c;
  --nav-bot:#3f3f3f;
}
*{box-sizing:border-box;margin:0;padding:0}
html,body{width:1200px;height:1041px;overflow:hidden}
body{position:relative;background:#fff;font-family:"PT Sans",Arial,sans-serif;color:var(--ink)}
.abs{position:absolute}
.topline{left:0;top:0;width:1200px;height:7px;background:#a6a6a6}

.brand{left:182px;top:34px;display:flex;align-items:center;gap:10px}
.brand-dot{width:22px;height:22px;border-radius:50%;background:var(--gold)}
.brand-name{font-size:33px;font-weight:700;color:var(--blue-deep);letter-spacing:1px}

.search{left:582px;top:63px;display:flex;align-items:center;gap:8px;font-size:11px;color:#444}
.search-field{width:175px;height:20px;border:1px solid #bbb;border-radius:3px;background:linear-gradient(#fff,#f0f0f0);position:relative}
.search-field svg{position:absolute;right:5px;top:3px}

.contact{right:185px;top:51px;text-align:right;font-size:12px;color:#555;line-height:19px}
.contact b{font-weight:400;color:var(--blue)}

.nav{left:180px;top:106px;width:840px;height:35px;border-radius:4px;background:linear-gradient(var(--nav-top),var(--nav-bot));border:1px solid #555}
.nav a{position:absolute;top:9px;color:#fff;font-size:12.5px;text-decoration:none;letter-spacing:-.3px}

.hero{left:180px;top:150px;width:840px;height:266px}
.hero-title{left:357px;top:228px;color:#fff;font-family:"Archivo Black",sans-serif;font-size:34px;letter-spacing:1px}
.hero-sub{left:200px;top:270px;width:350px;text-align:right;color:#fff;font-style:italic;font-weight:700;font-size:21px;line-height:31px;letter-spacing:-.8px}
.arrow{width:28px;height:28px}
.devices{left:585px;top:154px;width:380px;height:240px;border-radius:14px;
  background:
    radial-gradient(ellipse 30% 40% at 80% 45%,#d9dde2 0%,rgba(217,221,226,0) 100%),
    radial-gradient(ellipse 60% 85% at 28% 50%,#fbfbfc 0%,#eef0f2 55%,rgba(238,240,242,0) 100%),
    linear-gradient(100deg,#e9ecef 0%,#e1e5e8 45%,#6b7178 62%,#2b2f34 78%,#3a3f45 100%);
  box-shadow:0 8px 14px -8px rgba(0,40,80,.35)}

.promo{left:180px;top:438px;width:840px;height:68px;border-radius:4px;border:1px solid #e07800;background:linear-gradient(var(--orange-top),var(--orange-bot))}
.promo-text{left:39px;top:18px;font-family:"Archivo Black",sans-serif;color:#fff;font-size:21.5px;letter-spacing:.8px}
.try{left:607px;top:11px;width:216px;height:46px;border-radius:5px;background:linear-gradient(#8d8d8d,#3f3f3f);border:1px solid #333;color:#fff;font-family:"Archivo Black",sans-serif;font-size:22px;letter-spacing:1px;padding:6px 0 0 72px}
.try svg{position:absolute;left:8px;top:4px}

.video{left:179px;top:532px;width:216px;height:138px;border:1px solid #ccc;padding:5px;background:#fff}
.video-screen{width:100%;height:100%;background:radial-gradient(ellipse at 45% 55%,#2c5aa6,#0a0f22 60%,#000);position:relative}
.video-title{position:absolute;left:0;top:0;width:100%;height:22px;background:rgba(30,30,30,.85);color:#eee;font-size:13px;padding:3px 10px;font-family:Arial,sans-serif}
.play{position:absolute;left:84px;top:52px;width:38px;height:26px;border-radius:5px;background:#111;border:1px solid #444}
.play::after{content:"";position:absolute;left:15px;top:6px;border-left:11px solid #fff;border-top:7px solid transparent;border-bottom:7px solid transparent}

.welcome{left:411px;top:534px;font-family:"Archivo Black",sans-serif;font-size:21px;color:var(--gold)}
.welcome span{color:var(--blue-deep)}
.intro{left:415px;top:570px;width:290px;font-size:9.3px;line-height:15.4px;color:var(--muted)}

.news{left:717px;top:533px;width:303px;height:126px;border-radius:5px;background:var(--panel);padding:12px 18px}
.news h2{font-weight:400;font-size:18px;color:var(--link)}
.news p{font-size:9.3px;line-height:15.4px;color:var(--muted);margin-top:8px;letter-spacing:-.1px}
.news-form{display:flex;justify-content:space-between;margin-top:11px}
.news-input{width:180px;height:21px;border:1px solid #ccc;border-radius:3px;background:#fff;font-size:9px;color:#888;padding:4px 11px}
.btn{height:20px;border-radius:3px;background:linear-gradient(#3a95d9,#0d5fa6);color:#fff;font-size:9.5px;text-align:center;line-height:20px;border:1px solid #0a4f8c}
.news .btn{width:78px}

.band{left:0;top:771px;width:1200px;height:206px;background:var(--band)}
.footer{left:0;top:977px;width:1200px;height:64px;background:var(--footer)}

.sec-head{display:flex;align-items:center;gap:8px;top:692px}
.sec-head h3{font-weight:400;font-size:18px;color:var(--blue)}
.card{top:735px;width:267px;height:194px;border-radius:7px;background:linear-gradient(#e3e3e3,#fff 45%);padding:19px 16px 0}
.card-photo{height:75px;border-radius:6px}
.card p{font-size:9.1px;line-height:15.4px;color:#333;margin-top:16px;padding-left:5px;letter-spacing:-.15px}
.card .btn{position:absolute;right:15px;top:156px;width:70px}
.shadow{top:936px;width:240px;height:14px;border-radius:50%;background:radial-gradient(ellipse,rgba(0,0,0,.45),transparent 70%)}

.foot-links{left:180px;top:991px;display:flex;font-size:10.5px;color:#fff;letter-spacing:-.3px}
.foot-links span{padding:0 13px;border-left:1px solid #fff;line-height:11px}
.foot-links span:first-child{padding-left:0;border:none}
.copy{left:180px;top:1012px;font-size:10px;color:#fff;letter-spacing:-.3px}
.copy b{font-weight:400;color:#5fb4f0}
.social{left:939px;top:998px;display:flex;gap:5px}
.social i{width:23px;height:23px;border-radius:3px;background:linear-gradient(#7fb5df,#3f7fb8)}
</style>
</head>
<body>
<div class="abs topline"></div>

<header>
  <div class="abs brand"><div class="brand-dot"></div><div class="brand-name">billquarry!</div></div>
  <div class="abs search">Search :
    <div class="search-field"><svg width="14" height="14" viewBox="0 0 14 14"><circle cx="5.5" cy="5.5" r="4" fill="none" stroke="#555" stroke-width="1.6"/><line x1="8.5" y1="8.5" x2="13" y2="13" stroke="#555" stroke-width="2.2"/></svg></div>
  </div>
  <div class="abs contact">Call us : <b>00 0000 000 000</b><br>Email Us : <b>billquarry@info.example</b></div>
  <nav class="abs nav">
    <a style="left:24px">Home</a><a style="left:101px">Download</a><a style="left:197px">Buy Now</a><a style="left:286px">Features</a><a style="left:375px">About</a><a style="left:452px">Accounting</a><a style="left:555px">Contact</a>
  </nav>
</header>

<section>
  <svg class="abs hero" viewBox="0 0 840 266">
    <defs>
      <linearGradient id="sky" x1="0" y1="0" x2="0" y2="1"><stop offset="0" stop-color="#2a78c2"/><stop offset=".6" stop-color="#4ea2de"/><stop offset="1" stop-color="#8cc8f0"/></linearGradient>
      <radialGradient id="haze" cx=".22" cy=".2" r=".45"><stop offset="0" stop-color="#fff" stop-opacity=".6"/><stop offset="1" stop-color="#fff" stop-opacity="0"/></radialGradient>
    </defs>
    <path d="M4 0H836Q840 0 840 4V248Q420 285 0 248V4Q0 0 4 0Z" fill="url(#sky)"/>
    <path d="M4 0H836Q840 0 840 4V248Q420 285 0 248V4Q0 0 4 0Z" fill="url(#haze)" role="img" aria-label="Stylised cloudy sky"/>
  </svg>
  <div class="abs devices" role="img" aria-label="Tablet, phone and tablet showing the invoicing app screens"></div>
  <div class="abs hero-title">billquarry!</div>
  <div class="abs hero-sub">invoicing, billing, accounting &amp;<br>inventory software for YOUR business</div>
  <svg class="abs arrow" style="left:202px;top:267px" viewBox="0 0 28 28"><circle cx="14" cy="14" r="12.5" fill="rgba(255,255,255,.2)" stroke="#fff" stroke-width="1.5"/><path d="M16 8l-6 6 6 6" fill="none" stroke="#fff" stroke-width="2.5"/></svg>
  <svg class="abs arrow" style="left:973px;top:267px" viewBox="0 0 28 28"><circle cx="14" cy="14" r="12.5" fill="rgba(255,255,255,.2)" stroke="#fff" stroke-width="1.5"/><path d="M12 8l6 6-6 6" fill="none" stroke="#fff" stroke-width="2.5"/></svg>
</section>

<section class="abs promo">
  <div class="abs promo-text">Business software that fits YOUR business.</div>
  <div class="abs try">
    <svg width="62" height="42" viewBox="0 0 62 42"><rect x="4" y="20" width="50" height="18" rx="4" fill="#e6e9ec" stroke="#9aa"/><path d="M30 2v18M22 12l8 9 8-9" fill="none" stroke="#3fbf2a" stroke-width="5"/></svg>
    Try it Free
  </div>
</section>

<section>
  <div class="abs video"><div class="video-screen" role="img" aria-label="Video demonstration still"><div class="video-title">billquarry! Video Demonstration</div><div class="play"></div></div></div>
  <h1 class="abs welcome">Welcome to <span>Bill Quarry</span></h1>
  <p class="abs intro">The Tumbled Slate Company's billquarry! invoicing &amp; billing software is an easy-to-learn invoice program, with ALL the features you need for your business. It is not just an invoice software or billing software but Pro can also manage your inventory and accounting. Suitable for trades people, wholesalers, trading companies, manufacturers, professionals and internet businesses.</p>
  <div class="abs news">
    <h2>Newsletter</h2>
    <p>Be the first to try - send your e-mail address and receive notification as soon as launch date comes around.</p>
    <div class="news-form"><div class="news-input">Enter your Email ID :</div><div class="btn">Submit</div></div>
  </div>
</section>

<div class="abs band"></div>

<section>
  <div class="abs sec-head" style="left:186px"><svg width="28" height="36" viewBox="0 0 28 36"><circle cx="14" cy="9" r="7" fill="#e0a070"/><path d="M2 36Q2 19 14 19T26 36Z" fill="#c33"/></svg><h3>About Bill Quarry</h3></div>
  <div class="abs sec-head" style="left:472px"><svg width="30" height="40" viewBox="0 0 30 40"><path d="M7 12Q7 3 16 3T25 12Q25 18 17 22V28" fill="none" stroke="#3a9ad8" stroke-width="6" stroke-linecap="round"/><circle cx="17" cy="36" r="3.5" fill="#3a9ad8"/></svg><h3>Features</h3></div>
  <div class="abs sec-head" style="left:756px"><svg width="50" height="44" viewBox="0 0 50 44"><circle cx="28" cy="18" r="17" fill="#f2b01e"/><path d="M28 18V1A17 17 0 0 1 45 18Z" fill="#3a8fd6"/><path d="M28 18H45A17 17 0 0 1 33 34Z" fill="#6cbf3a"/><rect x="2" y="16" width="26" height="26" rx="3" fill="#ccd2d8" stroke="#889"/></svg><h3>Accounting</h3></div>

  <article class="abs card" style="left:180px"><div class="card-photo" role="img" aria-label="Business people in a meeting" style="background:radial-gradient(ellipse 35% 70% at 30% 45%,#c9a184 0%,rgba(201,161,132,0) 100%),radial-gradient(ellipse 30% 60% at 75% 40%,#e2c3a4 0%,rgba(226,195,164,0) 100%),linear-gradient(90deg,#9fb4c8 0%,#8f9aa6 35%,#d9d2c8 55%,#c9b49c 80%,#8a7262 100%)"></div><p>Lorem Ipsum is simply dummy text of the printing and typesetting industry. Lorem Ipsum has been the industry's standard dummy text ever since the 1500s,</p><div class="btn">Readmore</div></article>
  <article class="abs card" style="left:468px"><div class="card-photo" role="img" aria-label="Hands typing on a laptop keyboard" style="background:radial-gradient(ellipse 45% 45% at 55% 40%,#e9c6ae 0%,rgba(233,198,174,0) 100%),linear-gradient(170deg,#f7f3ef 0%,#efe6de 45%,#cfc8c2 65%,#6f7276 85%,#4a4d52 100%)"></div><p>Lorem Ipsum is simply dummy text of the printing and typesetting industry. Lorem Ipsum has been the industry's standard dummy text ever since the 1500s,</p><div class="btn">Readmore</div></article>
  <article class="abs card" style="left:753px"><div class="card-photo" role="img" aria-label="Hands reviewing printed charts with a pen" style="background:radial-gradient(ellipse 25% 55% at 10% 50%,#d6957a 0%,rgba(214,149,122,0) 100%),radial-gradient(ellipse 30% 60% at 90% 55%,#c38c70 0%,rgba(195,140,112,0) 100%),linear-gradient(160deg,#efeeec 0%,#f8f8f7 45%,#dfe6ee 65%,#9aa1a8 100%)"></div><p>Lorem Ipsum is simply dummy text of the printing and typesetting industry. Lorem Ipsum has been the industry's standard dummy text ever since the 1500s,</p><div class="btn">Readmore</div></article>

  <div class="abs shadow" style="left:193px"></div>
  <div class="abs shadow" style="left:481px"></div>
  <div class="abs shadow" style="left:767px"></div>
</section>

<footer>
  <div class="abs footer"></div>
  <div class="abs foot-links"><span>Home</span><span>Download</span><span>Buy Now</span><span>Features</span><span>About</span><span>Accounting</span><span>Contact</span></div>
  <div class="abs copy">© 2013 Copyright . <b>Bill Quarry</b>.  All rights reserved</div>
  <div class="abs social"><i></i><i></i><i></i></div>
</footer>
</body>
</html>
```